New boutique IT consultancy needs business card

I need a business card and logo for my IT consultancy business, called 'Quenmarlo' . I want it to make me look bigger than I am. I want it to look classy, and modern. Simple design, that will be easy for me to translate into my webpage etc. The business card should be bold, and different.

The logo should emphasise the 'y' as used in quenmarlo

Target Market(s)

IT divisions in other companies

Industry/Entity Type

Business

Contact Information for Business Card

Doreen Pakfield
Director
+61 437 918 205
dpakfield@quenmarlo-mail.test

```html
<!DOCTYPE html>
<html lang="en">
<head>
<meta charset="utf-8">
<title>Quenmarlo — Business Card</title>
<link rel="stylesheet" href="https://fonts.googleapis.com/css2?family=Barlow:ital,wght@0,400;0,500;1,400&display=swap">
<style>
  :root {
    --charcoal: #333333;
    --signal-yellow: #ffd02b;
    --paper: #ffffff;
    --ink: #111111;
    --ghost-grey: #9a9a9a;
    --canvas-bg: #ffffff;
    --edge: #ececec;
  }
  * { box-sizing: border-box; margin: 0; padding: 0; }
  html, body {
    width: 1200px;
    height: 1000px;
    overflow: hidden;
    background: var(--canvas-bg);
    font-family: "Barlow", Arial, sans-serif;
  }
  .sheet {
    position: relative;
    width: 1200px;
    height: 1000px;
  }
  .card {
    position: absolute;
    overflow: hidden;
  }
  .card--front {
    left: 290px;
    top: 120px;
    width: 602px;
    height: 344px;
    background: var(--charcoal);
  }
  .card--front .accent-wedge {
    position: absolute;
    inset: 0;
    width: 100%;
    height: 100%;
  }
  .wordmark {
    position: absolute;
    font-weight: 400;
    line-height: 1;
    white-space: nowrap;
    letter-spacing: 0.5px;
  }
  .card--front .wordmark {
    left: 80px;
    top: 68px;
    font-size: 64px;
    color: var(--paper);
  }
  .card--back {
    left: 293px;
    top: 487px;
    width: 599px;
    height: 342px;
    background: var(--paper);
    box-shadow: 0 0 0 1px var(--edge);
  }
  .contact {
    position: absolute;
    right: 66px;
    top: 66px;
    text-align: right;
    color: var(--ink);
  }
  .contact__name {
    display: flex;
    align-items: center;
    justify-content: flex-end;
    gap: 8px;
    font-size: 18px;
    font-weight: 500;
    letter-spacing: 0.6px;
    line-height: 24px;
  }
  .contact__marker {
    width: 18px;
    height: 18px;
    background: var(--signal-yellow);
  }
  .contact__role {
    font-size: 15px;
    font-style: italic;
    line-height: 18px;
  }
  .contact__details {
    margin-top: 12px;
    font-size: 18px;
    font-weight: 500;
    line-height: 23px;
  }
  .card--back .wordmark {
    left: 130px;
    top: 262px;
    font-size: 150px;
    color: var(--ghost-grey);
  }
  .sheet > .wordmark--signoff {
    left: 958px;
    top: 902px;
    font-size: 42px;
    color: var(--charcoal);
  }
</style>
</head>
<body>
  <main class="sheet">
    <section class="card card--front" aria-label="Card front">
      <svg class="accent-wedge" viewBox="0 0 602 344" preserveAspectRatio="none" aria-hidden="true">
        <polygon points="602,40 602,344 443,344" fill="var(--signal-yellow)"/>
      </svg>
      <div class="wordmark">quenmarlo</div>
    </section>

    <section class="card card--back" aria-label="Card back">
      <div class="contact">
        <p class="contact__name"><span class="contact__marker"></span>DOREEN PAKFIELD</p>
        <p class="contact__role">Director</p>
        <p class="contact__details">+61 437 918 205<br>dpakfield@quenmarlo-mail.test</p>
      </div>
      <div class="wordmark" aria-hidden="true">quenmarlo</div>
    </section>

    <div class="wordmark wordmark--signoff">quenmarlo</div>
  </main>
</body>
</html>
```